International Business that supplies Power solution in need of a new business card design

We need a business card design for a new company based in Houston, Texas (but has satellite locations in Cleveland, Ohio, Pensacola, Florida, Denver, Colorado and Denmark, Sweden). The company is called 'Tidewell Grid Systems' and we provide high end active harmonic filters. These filters provide a reliable, effective method to mitigate harmonics, getting them to the recommended levels. We would like to see the design use a color of blue (as the owner of the company's last name is Tellow). I am also leaning towards a green/blue (emerald) or any color that can describe the ocean. We want to evoke the warm feeling you get when looking at a beach (as we spend a lot of time on the water). Perhaps the logo could have something with a 6 pulse or EKG lines (google images has these as examples).. but this is not totally necessary either. Similar companies that we are working with are Lumivar and Doreth to give you a better idea.

Our Preliminary distribution centers:

Fernwick
Crestline Motor Parts
Ravello
Northway Gentry Formalwear
Pinecrest Outfit
Paperlark Cards
Gear Depot
Citrine Quarter
Quill & Hollow
Trout Ridge Store
Soap and Linen Lab
Pillow Tub & More
Volt Mart
Wide Bins
Stitch a Plush Studio
Merriford Jacket Depot
Rollicks
TW Marlo
Odette's Trinkets
Snaps
Farrow's
Lowcost Treads
Penny Grove
Tandem
Kinfolk Coin
Homestead Shoes
ParQo
Sprint Mark
Kelvrock
Sole Vault
Always 34
Play Hub
VLT
Heron Ridge
KIV
RT Marsh & Sons
Putt Planet
Quayside Supply
MOR
Craft Nook
Wrenbury
House Yard
Vorn
T Fleet
RL Foxley
Wil T Marsh
Dunmore's
Zshop
Brin's
Tavin
Pelts
Rosalind
Orvel
Quimby Exhaust
Ridgeway Tool
Desk Central
Desk Prime
Tidal Pier
Hanlon Motor Supply
Vel Dune
Thrift Boots
ZIP Lads
Paw Wise
Furlo
Clayworks Loft
Signal Hut
Well Mend
Sofas on Hand
Polymer Draw
VIA 47
Greta Salon Supply
Plimm
Dashwell
Morton's Novelty
Athletic Hall
Brewlight Coffee
Shade Kiosk
Pivot
The Lattice
Keepsake Works
Play N Co
Furrow Supply
QDL
Metro Threadhouse
Delphine's Silk
Nutri Globe
Corbetts
Corbetts
Keel Harbor

Reason: the finalists have not responsed to potential changes. Want to provide them more time to get back and resubmit.

Pivot Market(s)

Our primary target will be people ages 35-50 who are engineers or like-minded. This will need to catch the attention of the decision makers of our target markets (as listed below). Our Pivot Markets are: Hospitals Medical Institutions Universities Museums Sports Stadiums Ski Resorts Auto Manufacturing Plants Chip Manufacturing Plants Water and Waste Water Treatment Plants Pump Stations Manufacturing Plants w/Drives Steel Plants Distribution Centers Data Centers Office Buildings Shipbuilders High Speed Trains Movable Bridges Amusement Parks Engineering Firms Airports Cell Tower Installations Shale Plots Tool and Die Shops EDM Aluminum Extrusion Factories Electrical Utility Companies Injection Molding Plants Printing Presses, Newspapers and Magazines Polymer Draw Plants Telecom Centers QDL manufacturers Wire Manufacturing Plants Zoos and Aquariums Metal Heat Treat Facilities and Heat Equipment Manufacturers

Industry/Entity Type

Business

Requirements
Nice to have
• It would be nice if the back was a solid color.. perhaps with a design but not necessary.

The primary info on this first round should include the info below

Mark Tellow
Chief Executive Officer
direct: 330.555.0148
fax: 866.555.0192
mark.tellow@tgsexample.com

```html
<!DOCTYPE html>
<html lang="en">
<head>
<meta charset="utf-8">
<title>Tidewell Grid Systems — Business Card</title>
<link rel="stylesheet" href="https://fonts.googleapis.com/css2?family=Michroma&display=swap">
<style>
  :root {
    --page-bg: #e6e9ee;
    --navy: #163f86;
    --royal: #1f56a8;
    --sky: #3c9be0;
    --ice: #9fd2f5;
    --paper-top: #ffffff;
    --paper-bottom: #e4e7ec;
    --ink: #3a3f47;
    --ink-soft: #5b6068;
  }
  * { margin: 0; padding: 0; box-sizing: border-box; }
  html, body {
    width: 1059px; height: 1200px; overflow: hidden;
    background: var(--page-bg);
    font-family: "Michroma", sans-serif;
  }
  .canvas { position: relative; width: 1059px; height: 1200px; }

  .card {
    position: absolute; left: 90px; width: 880px; height: 510px;
    overflow: hidden;
    box-shadow: 0 10px 28px rgba(20, 40, 80, 0.22);
  }
  .card--front {
    top: 60px;
    background: linear-gradient(160deg, var(--paper-top) 0%, #f4f5f7 45%, var(--paper-bottom) 100%);
  }
  .card--back {
    top: 630px;
    background: linear-gradient(135deg, var(--royal) 0%, var(--navy) 100%);
  }

  .edge-band { position: absolute; left: 0; top: 0; width: 120px; height: 510px; }

  .brand { position: absolute; display: flex; align-items: center; }
  .brand__dot { border-radius: 50%; flex: none; }
  .brand__name { white-space: nowrap; letter-spacing: 0.5px; }

  .card--front .brand { left: 52px; top: 90px; }
  .card--front .brand__dot {
    width: 100px; height: 100px; margin-right: 26px;
    background: radial-gradient(circle at 40% 35%, var(--sky) 0%, var(--royal) 70%, var(--navy) 100%);
    box-shadow: 0 0 0 5px #ffffff, 0 0 0 8px var(--ice);
  }
  .card--front .brand__name { font-size: 29px; color: var(--navy); }

  .contact { position: absolute; left: 180px; top: 364px; list-style: none; }
  .contact__item {
    display: flex; align-items: center; height: 31px;
    font-size: 13px; letter-spacing: 1.4px; color: var(--ink);
    text-transform: uppercase;
  }
  .contact__icon {
    width: 18px; height: 18px; margin-right: 12px; flex: none;
    border-radius: 50%; background: var(--navy);
    display: flex; align-items: center; justify-content: center;
  }
  .contact__icon svg { width: 11px; height: 11px; }

  .person { position: absolute; right: 18px; top: 432px; text-align: right; }
  .person__name { font-size: 19px; letter-spacing: 3px; color: var(--navy); text-transform: uppercase; }
  .person__title { font-size: 14px; letter-spacing: 2px; color: var(--ink-soft); margin-top: 6px; }

  .back-orb {
    position: absolute; left: -10px; top: 0; width: 340px; height: 340px; border-radius: 50%;
    background: radial-gradient(circle at 38% 32%, #8fd0fb 0%, var(--sky) 40%, #1f6fc4 80%, #1a5aad 100%);
    box-shadow: 0 0 0 6px rgba(255,255,255,0.18);
  }
  .card--back .brand { right: 22px; bottom: 66px; }
  .card--back .brand__name { font-size: 26px; color: #ffffff; }
</style>
</head>
<body>
<main class="canvas">

  <section class="card card--front" aria-label="Business card front">
    <svg class="edge-band" viewBox="0 0 120 510" aria-hidden="true">
      <path d="M0 0 H52 C112 120 112 390 52 510 H0 Z" fill="var(--royal)"/>
      <path d="M62 0 C124 120 124 390 62 510" fill="none" stroke="var(--sky)" stroke-width="4"/>
    </svg>

    <div class="brand">
      <span class="brand__dot"></span>
      <span class="brand__name">Tidewell Grid Systems</span>
    </div>

    <ul class="contact">
      <li class="contact__item">
        <span class="contact__icon"><svg viewBox="0 0 12 12"><path d="M3 1l2 2-1 1.5c.7 1.4 1.8 2.5 3.5 3.5L9 7l2 2-1.5 2C5 10.5 1.5 7 1 2.5z" fill="#fff"/></svg></span>
        330.555.0148
      </li>
      <li class="contact__item">
        <span class="contact__icon"><svg viewBox="0 0 12 12"><rect x="2" y="4" width="8" height="5" fill="#fff"/><rect x="3.5" y="1.5" width="5" height="2.5" fill="#fff"/></svg></span>
        866.555.0192
      </li>
      <li class="contact__item">
        <span class="contact__icon"><svg viewBox="0 0 12 12"><rect x="1.5" y="3" width="9" height="6.5" fill="#fff"/><path d="M1.5 3l4.5 3.5L10.5 3" fill="none" stroke="var(--navy)" stroke-width="1"/></svg></span>
        mark.tellow@tgsexample.com
      </li>
      <li class="contact__item">
        <span class="contact__icon"><svg viewBox="0 0 12 12"><circle cx="6" cy="6" r="4.5" fill="none" stroke="#fff" stroke-width="1.2"/><path d="M1.5 6h9M6 1.5c-2 2.5-2 6.5 0 9M6 1.5c2 2.5 2 6.5 0 9" fill="none" stroke="#fff" stroke-width="1"/></svg></span>
        www.tgsexample.com
      </li>
    </ul>

    <div class="person">
      <p class="person__name">Mark Tellow</p>
      <p class="person__title">CEO</p>
    </div>
  </section>

  <section class="card card--back" aria-label="Business card back">
    <div class="back-orb"></div>
    <div class="brand">
      <span class="brand__name">Tidewell Grid Systems</span>
    </div>
  </section>

</main>
</body>
</html>
```